Life Coaching and Career Coaching company needs new website with bold, modern, videos

We need a whole new website that is heavy on video. We are a small company who sells personal wellbeing services like career coaching, life coaching, and group coaching programs. The programs all help people design a better life.
FULL BRIEF ATTACHED and STYLE GUIDE
Also, look at https://www.brightfennel.com/coaching and galdrove.com and https://www.marnwick.life/ for a small amount of inspiration.

Industry/Entity Type

personal well-being/life coaching/career coaching

Number of Pages Required

3 page

Other font styles liked:
• fonts are in the brief

Requirements
Must have
• read the brief please - it's all in there. (things like the look, feel, how it will have lots of video, etc,)
Nice to have
• something really different looking and breakthrough. visually stunning. very trustworthy. Please read the brief, its all in there.
Should not have
• should not look like other life coaching websites. must have video!

```html
<!DOCTYPE html>
<html lang="en">
<head>
<meta charset="utf-8">
<title>Life Shape Studio — Life &amp; Career Coaching</title>
<link rel="stylesheet" href="https://fonts.googleapis.com/css2?family=Righteous&family=Raleway:wght@400;500;600;700&family=Montserrat:wght@600;700;800&display=swap">
<style>
:root{
  --teal-dark:#0f4f55;
  --teal:#1d6e72;
  --teal-mid:#2b7f7a;
  --green:#3f8f6c;
  --blue:#23638f;
  --coral:#f0605e;
  --mint:#dcefee;
  --mint-text:#8de0c8;
  --ink:#1d3d40;
  --grey:#6d7b7c;
  --navy:#1f2a36;
  --white:#ffffff;
}
*{box-sizing:border-box;margin:0;padding:0}
html,body{width:1200px;height:3634px;overflow:hidden}
body{position:relative;font-family:"Raleway",sans-serif;color:var(--ink);background:var(--white)}
.abs{position:absolute}
.display{font-family:"Righteous",sans-serif}
.eyebrow{font-family:"Montserrat",sans-serif;font-weight:700;letter-spacing:4px;font-size:18px}
.btn{position:absolute;display:flex;align-items:center;justify-content:center;gap:10px;background:var(--coral);color:var(--white);font-family:"Montserrat",sans-serif;font-weight:700;font-size:15px;border-radius:5px}
.media{position:absolute}

.hero{left:0;top:0;width:1200px;height:585px;background:linear-gradient(100deg,#0e5a5d 0%,#1b6d6c 45%,#4d7b75 100%)}
.hero-photo{left:600px;top:0;width:600px;height:585px;background:linear-gradient(90deg,rgba(27,109,108,0) 0%,#6f8b84 35%,#9aa8a2 70%,#5d7470 100%)}
.topbar{left:0;top:0;width:1200px;height:58px;border-bottom:1px solid rgba(255,255,255,.25)}
.logo{font-family:"Montserrat",sans-serif;font-weight:700;color:var(--white);font-size:27px;letter-spacing:-0.5px;line-height:1}
.logo small{display:block;text-align:right;font-size:10px;letter-spacing:1px;font-weight:600;margin-top:2px}
.nav-link{top:20px;color:var(--white);font-family:"Montserrat",sans-serif;font-weight:600;font-size:14px}
.signin{left:943px;top:0;width:116px;height:58px;border-radius:0}
.hero-kicker{left:138px;top:203px;color:var(--white);font-family:"Righteous",sans-serif;font-size:21px}
.hero-kicker span{color:var(--coral);margin-right:10px}
.hero-title{left:138px;top:235px;color:var(--white);font-family:"Righteous",sans-serif;font-size:72px;line-height:80px;letter-spacing:1px;font-weight:400}
.vertical{left:1126px;top:410px;transform:rotate(-90deg);transform-origin:0 0;color:var(--white);font-family:"Montserrat",sans-serif;font-size:12px;letter-spacing:4px;font-weight:600;white-space:nowrap}

.center{left:0;width:1200px;text-align:center}
.section-label{color:var(--teal);}
.section-title{font-family:"Righteous",sans-serif;font-size:40px;color:var(--ink);font-weight:400}
.mission{left:629px;top:818px;width:390px;font-size:15.5px;line-height:27px;color:#4b5a5b}
.mission b{color:var(--ink);font-weight:700}
.check-row{left:629px;display:flex;gap:16px;align-items:flex-start;font-family:"Montserrat",sans-serif;font-weight:700;font-size:13px;color:var(--ink);line-height:21px;width:420px}
.check-row svg{flex:none}

.values{left:0;top:1205px;width:1200px;height:47px;display:flex;justify-content:center;align-items:center;gap:32px;font-family:"Montserrat",sans-serif;font-weight:800;font-size:25px;color:var(--ink);letter-spacing:.5px}
.values i{width:8px;height:8px;border-radius:50%;background:var(--coral)}

.programs{left:0;top:1252px;width:1200px;height:698px;background:linear-gradient(120deg,#3e8f6e 0%,#2a7d7d 45%,#23628f 100%)}
.card{position:absolute;top:1471px;width:258px;height:362px;background:var(--white);border-radius:8px}
.card-media{position:absolute;top:1452px;width:234px;height:239px;border:4px solid var(--teal);border-radius:8px;background:linear-gradient(160deg,#c9c2b7,#8d8f86 60%,#5f6a66)}
.play{position:absolute;width:56px;height:56px;border-radius:50%;background:rgba(255,255,255,.85);display:flex;align-items:center;justify-content:center}
.card-title{position:absolute;top:1707px;font-family:"Righteous",sans-serif;font-size:17px;color:var(--ink);font-weight:400}
.card-meta{position:absolute;top:1733px;font-family:"Montserrat",sans-serif;font-weight:700;font-size:9px;color:var(--teal);display:flex;gap:5px;align-items:center}
.card-rule{position:absolute;top:1752px;width:220px;height:1px;background:#dde4e4}
.card-text{position:absolute;top:1762px;width:222px;font-size:11.5px;line-height:17px;color:var(--grey)}
.card-btn{top:1820px;width:140px;height:31px;font-family:"Righteous",sans-serif;font-weight:400;font-size:15px}

.testi{position:absolute;background:var(--mint);border-radius:10px;overflow:hidden}
.testi-media{position:absolute;left:0;top:0;width:100%}
.quote{position:absolute;text-align:center;font-size:14px;line-height:20px;color:#3b4a4b}
.name{position:absolute;font-family:"Righteous",sans-serif;color:var(--teal);font-size:22px;text-align:center}

.cta{left:111px;top:2923px;width:976px;height:345px;border-radius:14px;background:linear-gradient(110deg,#1d5c84 0%,#236f80 50%,#3a8c6f 100%)}
.footer{left:0;top:3210px;width:1200px;height:424px;background:var(--navy)}
.foot-head{top:3356px;color:var(--white);font-family:"Montserrat",sans-serif;font-weight:700;font-size:13px;letter-spacing:1px;padding-left:12px;border-left:2px solid var(--white);line-height:16px}
.foot-link{color:#d6dde2;font-size:13.5px}
.social{top:3431px;width:22px;height:22px;border:1px solid #cfd6dc;border-radius:50%}
</style>
</head>
<body>

<section class="abs hero" aria-label="Hero"></section>
<div class="media hero-photo" role="img" aria-label="Photo of a smiling woman in a blazer at a desk holding glasses"></div>
<header class="abs topbar">
  <div class="abs logo" style="left:138px;top:12px">LIFE SHAPE<small>STUDIO</small></div>
  <a class="abs nav-link" style="left:677px">Who We Are</a>
  <a class="abs nav-link" style="left:809px">Our Programs</a>
  <a class="btn signin">Sign In <svg width="8" height="12" viewBox="0 0 8 12"><path d="M1 1l5 5-5 5" stroke="#fff" stroke-width="2" fill="none"/></svg></a>
</header>
<p class="abs hero-kicker"><span>»</span>Unlock Your Best Life with</p>
<h1 class="abs hero-title">LIFE SHAPE<br>STUDIO</h1>
<a class="btn" style="left:140px;top:431px;width:149px;height:50px">Get Started <svg width="8" height="12" viewBox="0 0 8 12"><path d="M1 1l5 5-5 5" stroke="#fff" stroke-width="2" fill="none"/></svg></a>
<div class="abs vertical">FIRST COACHING SESSION</div>
<svg class="abs" style="left:1106px;top:439px" width="56" height="56" viewBox="0 0 56 56"><circle cx="28" cy="28" r="27" fill="rgba(255,255,255,.25)" stroke="rgba(255,255,255,.6)"/><rect x="21" y="19" width="4" height="18" fill="var(--coral)"/><rect x="31" y="19" width="4" height="18" fill="var(--coral)"/></svg>

<p class="abs center eyebrow section-label" style="top:682px">WHO WE ARE</p>
<h2 class="abs center section-title" style="top:712px">Our Unique Approach</h2>
<div class="abs" style="left:161px;top:794px;width:400px;height:313px;background:var(--teal-dark);border-radius:6px"></div>
<div class="media" style="left:175px;top:805px;width:402px;height:316px;border-radius:6px;background:linear-gradient(135deg,#efe6dc,#d8c3ad 55%,#b9a592)" role="img" aria-label="Photo of a smiling woman in glasses holding a laptop"></div>
<p class="abs mission"><b>Our mission</b> is to develop your skills and confidence through personalized coaching and mentoring, empowering you to live a more fulfilled life by design and achieve the success you desire.</p>
<div class="abs check-row" style="top:956px"><svg width="27" height="27" viewBox="0 0 27 27"><circle cx="13.5" cy="13.5" r="13.5" fill="var(--coral)"/><path d="M8 14l4 4 7-8" stroke="#fff" stroke-width="2.4" fill="none"/></svg><span>Only Life Shape Studio Offers Both Life and Career Coaching Programs</span></div>
<div class="abs check-row" style="top:1011px"><svg width="27" height="27" viewBox="0 0 27 27"><circle cx="13.5" cy="13.5" r="13.5" fill="var(--coral)"/><path d="M8 14l4 4 7-8" stroke="#fff" stroke-width="2.4" fill="none"/></svg><span style="padding-top:2px">A Diverse Team of Sixteen Coaches</span></div>
<div class="abs check-row" style="top:1059px"><svg width="27" height="27" viewBox="0 0 27 27"><circle cx="13.5" cy="13.5" r="13.5" fill="var(--coral)"/><path d="M8 14l4 4 7-8" stroke="#fff" stroke-width="2.4" fill="none"/></svg><span style="padding-top:2px">Flexible Programs for Real Results</span></div>

<svg class="abs" style="left:0;top:1158px" width="1200" height="50" viewBox="0 0 1200 50"><polygon points="0,42 1200,0 1200,42" fill="var(--coral)"/><rect x="0" y="42" width="1200" height="4" fill="var(--teal)"/></svg>
<div class="abs values"><span>TRUST</span><i></i><span>CONFIDENCE</span><i></i><span>FULFILLMENT</span><i></i><span>ACHIEVEMENT</span></div>

<section class="abs programs" aria-label="Programs"></section>
<p class="abs eyebrow" style="left:62px;top:1337px;color:var(--mint-text)">PROGRAMS</p>
<h2 class="abs display" style="left:62px;top:1362px;font-size:37px;color:var(--white);font-weight:400">Life Shape Studio</h2>
<svg class="abs" style="left:1059px;top:1368px" width="36" height="36" viewBox="0 0 36 36"><circle cx="18" cy="18" r="17" fill="rgba(255,255,255,.35)"/><path d="M21 11l-7 7 7 7" stroke="var(--teal)" stroke-width="2.4" fill="none"/></svg>
<svg class="abs" style="left:1110px;top:1368px" width="36" height="36" viewBox="0 0 36 36"><circle cx="18" cy="18" r="17" fill="var(--coral)"/><path d="M15 11l7 7-7 7" stroke="#fff" stroke-width="2.4" fill="none"/></svg>

<div class="card" style="left:62px"></div>
<div class="card" style="left:337px"></div>
<div class="card" style="left:612px"></div>
<div class="card" style="left:887px"></div>

<div class="card-media" style="left:73px" role="img" aria-label="Video still of colleagues celebrating at a meeting table"><div class="play" style="left:85px;top:87px"><svg width="20" height="22" viewBox="0 0 20 22"><path d="M2 1l17 10L2 21z" fill="var(--coral)"/></svg></div></div>
<div class="card-media" style="left:348px;background:linear-gradient(160deg,#b7a794,#8e8475 60%,#5d6760)" role="img" aria-label="Video still of a curly-haired woman speaking"><div class="play" style="left:85px;top:87px"><svg width="20" height="22" viewBox="0 0 20 22"><path d="M2 1l17 10L2 21z" fill="var(--coral)"/></svg></div></div>
<div class="card-media" style="left:623px;background:linear-gradient(160deg,#d7d4cf,#8f8c88 55%,#2d2f33)" role="img" aria-label="Video still of a businesswoman holding a phone"><div class="play" style="left:85px;top:87px"><svg width="20" height="22" viewBox="0 0 20 22"><path d="M2 1l17 10L2 21z" fill="var(--coral)"/></svg></div></div>
<div class="card-media" style="left:898px;background:linear-gradient(160deg,#8fb6d9,#4f7fad 55%,#2d4f76)" role="img" aria-label="Video still of a woman smiling outside an office building"><div class="play" style="left:85px;top:87px"><svg width="20" height="22" viewBox="0 0 20 22"><path d="M2 1l17 10L2 21z" fill="var(--coral)"/></svg></div></div>

<h3 class="card-title" style="left:84px">Career Ignite</h3>
<h3 class="card-title" style="left:359px">Life Kickoff</h3>
<h3 class="card-title" style="left:634px">Whole Renewal</h3>
<h3 class="card-title" style="left:909px">Bespoke Growth</h3>

<p class="card-meta" style="left:84px"><svg width="9" height="9" viewBox="0 0 9 9"><circle cx="4.5" cy="4.5" r="3.8" stroke="var(--teal)" fill="none"/><path d="M4.5 2.5v2h1.5" stroke="var(--teal)" fill="none"/></svg>7-Week Program</p>
<p class="card-meta" style="left:359px"><svg width="9" height="9" viewBox="0 0 9 9"><circle cx="4.5" cy="4.5" r="3.8" stroke="var(--teal)" fill="none"/><path d="M4.5 2.5v2h1.5" stroke="var(--teal)" fill="none"/></svg>4-Week Program</p>
<p class="card-meta" style="left:634px"><svg width="9" height="9" viewBox="0 0 9 9"><circle cx="4.5" cy="4.5" r="3.8" stroke="var(--teal)" fill="none"/><path d="M4.5 2.5v2h1.5" stroke="var(--teal)" fill="none"/></svg>16-Week Program</p>
<p class="card-meta" style="left:909px"><svg width="9" height="9" viewBox="0 0 9 9"><circle cx="4.5" cy="4.5" r="3.8" stroke="var(--teal)" fill="none"/><path d="M4.5 2.5v2h1.5" stroke="var(--teal)" fill="none"/></svg>Tailored Program</p>

<div class="card-rule" style="left:84px"></div><div class="card-rule" style="left:359px"></div><div class="card-rule" style="left:634px"></div><div class="card-rule" style="left:909px"></div>

<p class="card-text" style="left:84px">Accelerate your professional growth with Career Ignite.</p>
<p class="card-text" style="left:359px">Embark on a focused journey of self-discovery and transformation.</p>
<p class="card-text" style="left:634px">Achieve fulfillment, balance, and success on a profound level.</p>
<p class="card-text" style="left:909px">Craft a personalized coaching program with our diverse team to meet goals.</p>

<a class="btn card-btn" style="left:121px">Learn More <svg width="18" height="18" viewBox="0 0 18 18"><circle cx="9" cy="9" r="8" fill="#fff"/><path d="M7.5 5.5l3.5 3.5-3.5 3.5" stroke="var(--coral)" stroke-width="2" fill="none"/></svg></a>
<a class="btn card-btn" style="left:396px">Learn More <svg width="18" height="18" viewBox="0 0 18 18"><circle cx="9" cy="9" r="8" fill="#fff"/><path d="M7.5 5.5l3.5 3.5-3.5 3.5" stroke="var(--coral)" stroke-width="2" fill="none"/></svg></a>
<a class="btn card-btn" style="left:671px">Learn More <svg width="18" height="18" viewBox="0 0 18 18"><circle cx="9" cy="9" r="8" fill="#fff"/><path d="M7.5 5.5l3.5 3.5-3.5 3.5" stroke="var(--coral)" stroke-width="2" fill="none"/></svg></a>
<a class="btn card-btn" style="left:946px">Learn More <svg width="18" height="18" viewBox="0 0 18 18"><circle cx="9" cy="9" r="8" fill="#fff"/><path d="M7.5 5.5l3.5 3.5-3.5 3.5" stroke="var(--coral)" stroke-width="2" fill="none"/></svg></a>

<p class="abs center eyebrow section-label" style="top:2061px">VIDEO TESTIMONIALS</p>
<h2 class="abs center section-title" style="top:2088px">Real Stories, Real Results</h2>
<p class="abs" style="left:270px;top:2148px;width:660px;text-align:center;font-size:15.5px;line-height:27px;color:#3b4a4b">Listen to the inspiring journeys of individuals like you who have transformed their lives with Life Shape Studio.</p>

<div class="testi" style="left:-1px;top:2288px;width:300px;height:426px">
  <div class="testi-media" style="height:320px;background:linear-gradient(160deg,#eee7e2,#cbbcb2 60%,#8c7b73)" role="img" aria-label="Video still of a smiling woman in a dark sweater"></div>
  <div class="play" style="left:62px;top:302px;width:60px;height:60px;background:#fff"><svg width="20" height="22" viewBox="0 0 20 22"><path d="M2 1l17 10L2 21z" fill="var(--coral)"/></svg></div>
  <p class="quote" style="left:-120px;top:350px;width:370px;font-size:13px">"The 7-week program gave me the clarity and confidence to pursue my dreams fearlessly."</p>
  <p class="name" style="left:0;top:390px;width:180px">Sarah</p>
</div>

<div class="testi" style="left:331px;top:2242px;width:536px;height:517px">
  <div class="testi-media" style="height:388px;background:linear-gradient(160deg,#a9b594,#6e7a5c 50%,#3a3a34)" role="img" aria-label="Video still of a young woman in sunglasses making peace signs"></div>
  <div class="play" style="left:230px;top:322px;width:76px;height:76px;background:#fff"><svg width="26" height="28" viewBox="0 0 20 22"><path d="M2 1l17 10L2 21z" fill="var(--coral)"/></svg></div>
  <svg class="abs" style="left:80px;top:420px" width="90" height="70" viewBox="0 0 90 70"><path d="M5 70V40Q5 10 35 5v12Q20 22 20 35h15v35zM50 70V40Q50 10 80 5v12Q65 22 65 35h15v35z" fill="rgba(255,255,255,.6)"/></svg>
  <p class="quote" style="left:78px;top:418px;width:380px;font-size:16px;line-height:24px">"In 7 weeks, I achieved career milestones I never thought possible."</p>
  <p class="name" style="left:0;top:470px;width:536px;font-size:26px">Jenny</p>
</div>

<div class="testi" style="left:900px;top:2288px;width:301px;height:426px">
  <div class="testi-media" style="height:320px;background:linear-gradient(160deg,#4e4c48,#77716a 50%,#c9c7c2)" role="img" aria-label="Video still of a smiling grey-haired man in a white shirt"></div>
  <div class="play" style="left:185px;top:272px;width:60px;height:60px;background:#fff"><svg width="20" height="22" viewBox="0 0 20 22"><path d="M2 1l17 10L2 21z" fill="var(--coral)"/></svg></div>
  <p class="quote" style="left:60px;top:340px;width:380px;font-size:13px">"The 16-week program was transformative. I'm living a more fulfilling life."</p>
  <p class="name" style="left:152px;top:385px;width:140px">Michael</p>
</div>

<svg class="abs" style="left:565px;top:2800px" width="70" height="14" viewBox="0 0 70 14"><circle cx="5" cy="7" r="2.5" fill="#cfd6d6"/><circle cx="19" cy="7" r="2.5" fill="#cfd6d6"/><circle cx="35" cy="7" r="4.5" fill="none" stroke="var(--coral)" stroke-width="2"/><circle cx="51" cy="7" r="2.5" fill="#cfd6d6"/><circle cx="65" cy="7" r="2.5" fill="#cfd6d6"/></svg>

<footer class="abs footer"></footer>
<section class="abs cta" aria-label="Get started"></section>
<div class="media" style="left:761px;top:2841px;width:226px;height:427px;border-radius:110px 110px 0 0;background:linear-gradient(180deg,#c9c3bc 0%,#2b3b5a 40%,#1f2d48 100%)" role="img" aria-label="Photo of a smiling coach in a navy suit holding a clipboard"></div>
<p class="abs eyebrow" style="left:182px;top:2994px;color:var(--mint-text)">GET STARTED</p>
<h2 class="abs display" style="left:182px;top:3024px;font-size:38px;color:var(--white);font-weight:400">Start Your Journey</h2>
<p class="abs" style="left:182px;top:3090px;width:460px;color:#e8f0f0;font-size:15px;line-height:27px">Invest in yourself and your future. Join Life Shape Studio for a journey of self-discovery, growth, and success.</p>
<a class="btn" style="left:182px;top:3170px;width:149px;height:49px">Get Started <svg width="8" height="12" viewBox="0 0 8 12"><path d="M1 1l5 5-5 5" stroke="#fff" stroke-width="2" fill="none"/></svg></a>

<div class="abs logo" style="left:138px;top:3362px">LIFE SHAPE<small>STUDIO</small></div>
<span class="abs social" style="left:140px"></span>
<span class="abs social" style="left:171px"></span>
<span class="abs social" style="left:202px"></span>
<span class="abs social" style="left:233px"></span>

<p class="abs foot-head" style="left:477px">MAIN LINK</p>
<a class="abs foot-link" style="left:477px;top:3397px">Who We Are</a>
<a class="abs foot-link" style="left:477px;top:3427px">Our Programs</a>
<a class="abs foot-link" style="left:477px;top:3457px">Contact Us</a>
<a class="abs foot-link" style="left:477px;top:3487px">Testimonials</a>

<p class="abs foot-head" style="left:678px">OUR PROGRAMS</p>
<a class="abs foot-link" style="left:678px;top:3397px">Career Ignite</a>
<a class="abs foot-link" style="left:678px;top:3427px">Life Kickoff</a>
<a class="abs foot-link" style="left:678px;top:3457px">Whole Renewal</a>
<a class="abs foot-link" style="left:678px;top:3487px">Bespoke Growth</a>

<p class="abs foot-head" style="left:956px">COMPANY</p>
<a class="abs foot-link" style="left:956px;top:3397px">About Us</a>
<a class="abs foot-link" style="left:956px;top:3427px">Privacy Policy</a>
<a class="abs foot-link" style="left:956px;top:3457px">Testimonials</a>

<div class="abs" style="left:143px;top:3559px;width:914px;height:1px;background:#4a5563"></div>
<p class="abs center" style="top:3580px;color:#c9d1d8;font-size:13px">© 2023 All Rights Reserved | Life Shape Studio</p>

</body>
</html>
```